Linen Sparrow- Hand made fashion accessories

Linen sparrow is a new business that will be selling hand made fashion accessories for women such as bags, baskets, knecklaces etc. The items are all hand made from Africa. I would like natural colors leaning more to the cardboard rustic look. I would like the card to look simple but elegant at the same time.

Industry/Entity Type

Business

Contact Information for Business Card

www.linensparrow-example.com.au
sales@linensparrow-example.com.au
Tel: 0427586302

Font styles to use
Decorative
Script

Requirements
Must have
• Earthy and rustic colours. Straw, cardboard etc. Fine black cursive print. One side of card only name
• second side website, email and tel.
Should not have
• No need to have any description of what business sells or does. No pictures of anything.

```html
<!DOCTYPE html>
<html lang="en">
<head>
<meta charset="utf-8">
<title>Linen Sparrow — Business Card</title>
<link rel="stylesheet" href="https://fonts.googleapis.com/css2?family=Italianno&family=Cormorant+Garamond:ital,wght@1,500&display=swap">
<style>
  :root {
    --page-bg: #f3f2f0;
    --card-kraft: #c9a97c;
    --card-kraft-deep: #bd9c6d;
    --pattern-straw: #c4a372;
    --pattern-straw-light: #d3b98d;
    --rule-ink: #231d17;
    --ink-black: #1c1814;
    --card-shadow: rgba(0, 0, 0, 0.28);
  }
  html, body {
    margin: 0;
    padding: 0;
    width: 1200px;
    height: 1000px;
    overflow: hidden;
    background: var(--page-bg);
  }
  .canvas {
    position: relative;
    width: 1200px;
    height: 1000px;
  }
  .card {
    position: absolute;
    width: 325px;
    height: 521px;
    box-shadow: 0 1px 3px var(--card-shadow);
    overflow: hidden;
  }
  .card--front {
    left: 238px;
    top: 265px;
    background: var(--card-kraft);
  }
  .card--back {
    left: 616px;
    top: 266px;
    background: linear-gradient(160deg, var(--card-kraft) 0%, var(--card-kraft-deep) 100%);
  }
  .pattern-field {
    position: absolute;
    left: 0;
    width: 100%;
    background: linear-gradient(180deg, var(--pattern-straw-light), var(--pattern-straw));
  }
  .pattern-field--top { top: 0; height: 201px; }
  .pattern-field--bottom { top: 323px; height: 198px; }
  .name-band {
    position: absolute;
    left: 0;
    top: 201px;
    width: 100%;
    height: 122px;
    background: var(--card-kraft);
    border-top: 2px solid var(--rule-ink);
    border-bottom: 2px solid var(--rule-ink);
    box-sizing: border-box;
    display: flex;
    align-items: center;
    justify-content: center;
  }
  .brand-name {
    margin: 0;
    font-family: "Italianno", cursive;
    font-weight: 400;
    font-size: 58px;
    color: var(--ink-black);
    letter-spacing: 1px;
  }
  .contact-list {
    position: absolute;
    left: 0;
    top: 194px;
    width: 100%;
    margin: 0;
    padding: 0;
    list-style: none;
    text-align: center;
    font-family: "Cormorant Garamond", serif;
    font-style: italic;
    font-weight: 500;
    font-size: 21px;
    line-height: 42px;
    color: var(--ink-black);
  }
</style>
</head>
<body>
<main class="canvas">
  <section class="card card--front">
    <div class="pattern-field pattern-field--top" role="img" aria-label="Repeating small floral pattern in pale straw"></div>
    <div class="name-band">
      <h1 class="brand-name">Linen Sparrow</h1>
    </div>
    <div class="pattern-field pattern-field--bottom" role="img" aria-label="Repeating small floral pattern in pale straw"></div>
  </section>
  <section class="card card--back">
    <ul class="contact-list">
      <li class="contact-phone">0427-586-302</li>
      <li class="contact-web">www.linensparrow-example.com.au</li>
      <li class="contact-email">sales@linensparrow-example.com.au</li>
    </ul>
  </section>
</main>
</body>
</html>
```